List Now, Launch Later - DL Flyer front & back

Looking for a flyer that has nothing much other than “List Now, Launch Later” on the front with text to fill the back. With image on front that symbolises launch, maybe house being launch like a rocket.
The text has yet to be written but here is the gist: This is for the back of flyer.
List property and delay the launch. In the meantime, we can:
· Prepare contract
· Prepare marketing
· Prepare the property
· Do the Pest and Building Report
· Give the tenants their due notice of sale
· Advise buyers in an off market capacity
This ensures we are first to market when the time comes rather than coming onto the market along with a surge of spring sellers. Buyers are still buying now. The lack of stock is inadvertently creating strength in the market.
The feel has to be modern, clean, contemporary & graphic

```html
<!DOCTYPE html>
<html lang="en">
<head>
<meta charset="utf-8">
<title>List Now, Launch Later – DL Flyer</title>
<link rel="stylesheet" href="https://fonts.googleapis.com/css2?family=Teko:wght@400;500;600&family=Saira+Condensed:wght@400&family=Nunito:wght@600;700&display=swap">
<style>
  :root {
    --navy-deep: #0b1f4f;
    --navy: #14377a;
    --navy-bright: #1f57a6;
    --red: #e41b2c;
    --red-dark: #a5141f;
    --white: #ffffff;
    --icon-red: #e8404a;
    --gap: #050a18;
  }
  * { margin: 0; padding: 0; box-sizing: border-box; }
  html, body { width: 1200px; height: 838px; overflow: hidden; background: var(--gap); }
  .flyer { position: relative; width: 1200px; height: 838px; }

  /* Front panel */
  .front {
    position: absolute; left: 0; top: 0; width: 596px; height: 838px; overflow: hidden;
    background: radial-gradient(circle at 30% 20%, var(--navy-bright) 0%, var(--navy) 45%, var(--navy-deep) 100%);
  }
  .front-artwork {
    position: absolute; left: 0; top: 60px; width: 520px; height: 760px;
    background:
      radial-gradient(ellipse 120px 110px at 340px 230px, rgba(255,90,70,.85), rgba(255,60,60,0) 100%),
      radial-gradient(ellipse 90px 320px at 170px 520px, rgba(255,120,200,.55), rgba(80,160,255,.25) 60%, rgba(0,0,0,0) 100%);
  }
  .front-title {
    position: absolute; right: 58px; top: 594px; text-align: right; white-space: nowrap;
    font-family: "Teko", sans-serif; font-weight: 600; font-size: 92px; line-height: 100px;
    color: var(--white); letter-spacing: 0;
  }
  .front-title .line { display: block; }
  .front-title .accent { color: var(--red); }

  /* Back panel */
  .back {
    position: absolute; left: 604px; top: 0; width: 596px; height: 838px; overflow: hidden;
    background: linear-gradient(160deg, var(--navy-bright) 0%, var(--navy) 35%, var(--navy-deep) 80%);
  }
  .back-heading {
    position: absolute; left: 0; top: 58px; width: 596px; text-align: center; white-space: nowrap;
    font-family: "Teko", sans-serif; font-weight: 500; font-size: 48px; line-height: 48px; color: var(--white);
  }
  .services { position: absolute; left: 0; top: 0; width: 596px; }
  .service { position: absolute; width: 190px; text-align: center; }
  .service svg { display: block; margin: 0 auto; width: 70px; height: 70px; }
  .service-label {
    margin-top: 14px; font-family: "Saira Condensed", sans-serif; font-size: 20px; line-height: 23px; color: var(--white); white-space: nowrap;
  }
  .band { position: absolute; left: 0; top: 0; width: 596px; height: 838px; }

  .find-us {
    position: absolute; left: 46px; top: 716px;
    font-family: "Nunito", sans-serif; font-weight: 600; font-size: 22px; color: var(--white);
  }
  .social { position: absolute; left: 46px; top: 756px; display: flex; gap: 14px; }
  .social-item { display: flex; align-items: center; gap: 6px; font-family: "Nunito", sans-serif; font-weight: 700; font-size: 13px; color: var(--white); }
  .social-dot { width: 22px; height: 22px; border-radius: 50%; background: var(--white); }

  .contact { position: absolute; right: 42px; top: 690px; text-align: right; list-style: none; }
  .contact li {
    display: flex; justify-content: flex-end; align-items: center; gap: 8px; white-space: nowrap;
    font-family: "Nunito", sans-serif; font-weight: 700; font-size: 20px; line-height: 27px; color: var(--white);
  }
  .contact svg { width: 16px; height: 16px; fill: var(--white); }
</style>
</head>
<body>
<div class="flyer">

  <section class="front">
    <div class="front-artwork" role="img" aria-label="Toy house blasting off through a starry sky like a rocket, trailing a rainbow light streak"></div>
    <h1 class="front-title">
      <span class="line"><span class="accent">LIST</span> NOW,</span>
      <span class="line"><span class="accent">LAUNCH</span> LATER</span>
    </h1>
  </section>

  <section class="back">
    <svg class="band" viewBox="0 0 596 838" aria-hidden="true">
      <defs>
        <linearGradient id="redFill" x1="0" y1="0" x2="1" y2="0">
          <stop offset="0" stop-color="#b3151f"/>
          <stop offset=".5" stop-color="#d41a28"/>
          <stop offset="1" stop-color="#e41b2c"/>
        </linearGradient>
      </defs>
      <path d="M0 640 C220 630 430 590 596 485 L596 500 C430 605 220 650 0 662 Z" fill="#0a1c40" opacity=".9"/>
      <path d="M0 650 C220 640 440 600 596 512 L596 838 L0 838 Z" fill="url(#redFill)"/>
    </svg>

    <h2 class="back-heading">List Property and Delay the Launch.<br>In the meantime, we can :</h2>

    <div class="services">
      <div class="service" style="left:9px; top:216px;">
        <svg viewBox="0 0 70 70" fill="none" stroke="var(--icon-red)" stroke-width="2.2">
          <rect x="14" y="4" width="36" height="62" rx="3"/>
          <line x1="20" y1="18" x2="42" y2="18"/><line x1="20" y1="25" x2="42" y2="25"/><line x1="20" y1="32" x2="36" y2="32"/>
          <line x1="62" y1="24" x2="36" y2="56"/><line x1="36" y1="56" x2="33" y2="62"/>
        </svg>
        <p class="service-label">Prepare<br>Contract</p>
      </div>
      <div class="service" style="left:195px; top:216px;">
        <svg viewBox="0 0 70 70" fill="none" stroke="var(--icon-red)" stroke-width="2.2">
          <rect x="4" y="8" width="62" height="42" rx="3"/>
          <rect x="10" y="14" width="50" height="30"/>
          <line x1="30" y1="50" x2="28" y2="60"/><line x1="40" y1="50" x2="42" y2="60"/><line x1="18" y1="62" x2="52" y2="62"/>
          <path d="M15 30 L24 22 L33 30 M18 30 V38 H30 V30"/>
          <line x1="38" y1="24" x2="54" y2="24"/><line x1="38" y1="30" x2="54" y2="30"/><line x1="38" y1="36" x2="50" y2="36"/>
        </svg>
        <p class="service-label">Prepare<br>Marketing</p>
      </div>
      <div class="service" style="left:381px; top:216px;">
        <svg viewBox="0 0 70 70" fill="none" stroke="var(--icon-red)" stroke-width="2.2">
          <circle cx="35" cy="35" r="32"/>
          <path d="M12 36 L26 26 L36 32 L46 26 L58 36 L44 48 L26 48 Z"/>
          <line x1="35" y1="8" x2="35" y2="16"/><line x1="24" y1="12" x2="27" y2="18"/><line x1="46" y1="12" x2="43" y2="18"/>
        </svg>
        <p class="service-label">Prepare<br>the Property</p>
      </div>

      <div class="service" style="left:9px; top:388px;">
        <svg viewBox="0 0 70 70" fill="none" stroke="var(--icon-red)" stroke-width="2.2">
          <path d="M10 4 H48 V54 L36 66 H10 Z"/>
          <line x1="16" y1="14" x2="38" y2="14"/><line x1="16" y1="22" x2="40" y2="22"/><line x1="16" y1="30" x2="34" y2="30"/><line x1="16" y1="38" x2="30" y2="38"/>
          <line x1="62" y1="16" x2="36" y2="48"/><line x1="36" y1="48" x2="33" y2="54"/>
        </svg>
        <p class="service-label">Do the Pest and<br>Building Report</p>
      </div>
      <div class="service" style="left:195px; top:383px;">
        <svg viewBox="0 0 70 70" fill="none" stroke="var(--icon-red)" stroke-width="2.2">
          <rect x="8" y="2" width="54" height="40"/>
          <line x1="16" y1="12" x2="54" y2="12"/><line x1="16" y1="20" x2="54" y2="20"/><line x1="16" y1="28" x2="44" y2="28"/>
          <rect x="27" y="42" width="16" height="16"/>
          <line x1="10" y1="66" x2="60" y2="66"/><line x1="22" y1="58" x2="48" y2="58"/>
        </svg>
        <p class="service-label">Give the tenants<br>their due notice of sale</p>
      </div>
      <div class="service" style="left:381px; top:388px;">
        <svg viewBox="0 0 70 70" fill="none" stroke="var(--icon-red)" stroke-width="2.2">
          <rect x="6" y="26" width="18" height="40" rx="3"/>
          <rect x="46" y="26" width="18" height="40" rx="3"/>
          <path d="M28 34 H42 M38 30 L42 34 L38 38"/>
          <path d="M42 46 H28 M32 42 L28 46 L32 50"/>
        </svg>
        <p class="service-label">Advise Buyers in an<br>off Market Capacity</p>
      </div>
    </div>

    <p class="find-us">Find us on:</p>
    <div class="social">
      <span class="social-item"><span class="social-dot"></span>Nestbook</span>
      <span class="social-item"><span class="social-dot"></span>Linkup</span>
    </div>

    <ul class="contact">
      <li><svg viewBox="0 0 16 16"><path d="M8 0a5.5 5.5 0 0 0-5.5 5.5C2.5 10 8 16 8 16s5.5-6 5.5-10.5A5.5 5.5 0 0 0 8 0zm0 8a2.5 2.5 0 1 1 0-5 2.5 2.5 0 0 1 0 5z"/></svg>45 orbitlistgroup</li>
      <li><svg viewBox="0 0 16 16"><path d="M0 3h16v10H0zM1.5 4.2 8 9l6.5-4.8V4.5L8 9.6 1.5 4.5z" fill-rule="evenodd"/></svg>hello@orbitlistgroup</li>
      <li><svg viewBox="0 0 16 16"><path d="M3 0l3 4-2 2c1 2.5 3.5 5 6 6l2-2 4 3-2 3C7 16 0 9 0 3z"/></svg>01987 65432</li>
      <li><svg viewBox="0 0 16 16"><path d="M2 0l12 9-5 .5 3 6-2 .5-3-6L2 14z"/></svg>www.orbitlistgroup.com</li>
    </ul>
  </section>

</div>
</body>
</html>
```